Vardelix is a financial services company which transacts by allowing clients to purchase Quorbit (c

I need a divi themed site (if possible) but I can work with html as well since I have paid for the CSS very simple that will simply show what vardelix is and what we graphically need to do in order to make the transaction happen

Target Market(s)

Any persons over the age of 18 globally who wants to purchase Quorbit (crypto currency) with their credit cards and receive a quorb wallet from Vardelix

Industry/Entity Type

Insurance

Coding

Coded - Design and coding required

Number of Pages Required

3 page

Font styles to use
Serif

Colors
3277b5
3176b5
85acd3
85cae6

Requirements
Must have
• Logo visible top let on all pages ... color scheme that evokes trust, confidence, transparency.. terms and conditions and privacy policy footer links
Nice to have
• I willl have logo chosen in next 24 hrs..

```html
<!DOCTYPE html>
<html lang="en">
<head>
<meta charset="utf-8">
<title>Vardelix – From Credit Card to Quorbit</title>
<link href="https://fonts.googleapis.com/css2?family=Roboto:wght@300;400;500;700&family=Open+Sans:wght@300;400;600&display=swap" rel="stylesheet">
<style>
:root{
  --blue:#3277b5;
  --blue-light:#85cae6;
  --blue-soft:#85acd3;
  --navy-deep:#0f2b48;
  --grey:#f2f2f2;
  --text:#555;
  --white:#fff;
}
*{box-sizing:border-box;margin:0;padding:0}
html,body{width:684px;height:1200px;overflow:hidden}
body{position:relative;background:var(--white);font-family:"Open Sans",sans-serif;color:var(--text)}
.abs{position:absolute}

/* header */
.site-header{left:0;top:0;width:684px;height:47px;background:var(--white)}
.brand{left:92px;top:15px;display:flex;align-items:center;gap:6px;font-family:"Roboto",sans-serif;font-weight:500;font-size:15px;line-height:17px;color:var(--blue);letter-spacing:.5px}
.brand-mark{width:10px;height:10px;border-radius:50%;background:var(--blue)}
.main-nav{left:425px;top:0;height:47px;display:flex}
.nav-item{height:47px;display:flex;flex-direction:column;align-items:center;justify-content:center;gap:6px;padding:0 8px;font-family:"Roboto",sans-serif;font-size:6.5px;letter-spacing:1px;color:#333;text-transform:uppercase}
.nav-item svg{width:6px;height:6px}
.nav-item.is-active{background:var(--blue);color:var(--white);width:38px;padding:0}

/* hero */
.hero{left:0;top:47px;width:684px;height:321px;background:radial-gradient(ellipse at 40% 55%,#4f6f8f 0%,#2d3f55 45%,#141c28 100%)}
.hero-title{left:0;width:684px;top:92px;text-align:center;font-family:"Roboto",sans-serif;font-weight:300;font-size:30px;line-height:38px;color:var(--white);letter-spacing:.5px}
.hero-title strong{font-weight:700;color:var(--blue-light)}
.hero-sub{left:0;width:684px;top:184px;text-align:center;font-family:"Roboto",sans-serif;font-size:10px;letter-spacing:2px;color:var(--white)}
.btn-learn{left:294px;top:220px;width:96px;height:31px;background:var(--white);display:flex;align-items:center;justify-content:center;gap:14px;font-family:"Roboto",sans-serif;font-size:6px;letter-spacing:1px;color:var(--blue)}
.slider-arrow{top:158px;width:25px;height:24px;background:var(--white);display:flex;align-items:center;justify-content:center}
.slider-arrow.prev{left:13px}.slider-arrow.next{left:647px}

/* features */
.features{left:0;top:368px;width:684px;height:110px;background:linear-gradient(135deg,#3a7bbd,#4a8acb 50%,#3977b9);display:flex}
.feature{width:171px;height:110px;position:relative;display:flex;flex-direction:column;align-items:center;padding-top:18px}
.feature+.feature::before{content:"";position:absolute;left:0;top:10px;height:90px;width:1px;background:rgba(255,255,255,.35)}
.feature svg{width:42px;height:42px}
.feature p{margin-top:11px;text-align:center;font-family:"Roboto",sans-serif;font-size:7.5px;line-height:10px;letter-spacing:1.3px;color:var(--white);text-transform:uppercase;padding:0 12px}

/* section titles */
.section-title{left:0;width:684px;text-align:center;font-family:"Roboto",sans-serif;font-weight:500;font-size:17px}
.section-title .lead{color:var(--blue-light)}
.why-title{top:506px}.why-title .rest{color:var(--blue)}

/* split */
.benefits{left:0;top:556px;width:341px;height:249px;background:var(--grey)}
.benefit-list{right:362px;top:607px;list-style:none;text-align:right}
.benefit-list li{font-size:8.5px;line-height:20px;color:#555;display:flex;justify-content:flex-end;align-items:center;gap:8px}
.benefit-list li::before{content:"";width:6px;height:6px;border-radius:50%;background:var(--blue);box-shadow:inset 0 0 0 1.5px var(--blue),inset 0 0 0 3px #fff}
.btn-primary{left:181px;top:728px;width:141px;height:25px;background:var(--blue);display:flex;align-items:center;justify-content:center;gap:10px;font-family:"Roboto",sans-serif;font-size:7.5px;letter-spacing:1.5px;color:var(--white)}
.video-media{left:341px;top:556px;width:343px;height:249px;background:linear-gradient(135deg,#4a3f8c 0%,#6b4fa6 40%,#8a6fb8 70%,#c0a070 100%)}

/* testimonials */
.testimonials{left:0;top:827px;width:684px;height:256px;background:linear-gradient(180deg,#1a4166,#123456)}
.testi-title{top:851px}.testi-title .rest{color:var(--white)}
.testi-card{top:937px;width:158px;height:119px;background:var(--white);border-radius:2px;text-align:center;padding-top:48px}
.testi-card .quote{font-family:"Roboto",sans-serif;font-weight:700;font-size:28px;line-height:16px;height:14px;color:#d0d0d0}
.testi-card p{margin-top:8px;font-size:6px;line-height:10.5px;color:#555;padding:0 11px}
.testi-card cite{display:block;margin-top:2px;font-size:5.6px;font-style:italic;font-weight:600;color:var(--blue)}
.avatar{top:899px;width:72px;height:72px;border-radius:50%;border:3px solid var(--blue);background:radial-gradient(circle at 50% 40%,#d8c2ad,#9a8472)}

/* footer */
.site-footer{left:0;top:1107px;width:684px;height:93px;background:var(--navy-deep)}
.footer-nav{left:0;width:684px;top:1129px;display:flex;justify-content:center;gap:18px;font-family:"Roboto",sans-serif;font-size:6.5px;letter-spacing:1px;color:var(--white)}
.footer-rule{left:92px;top:1155px;width:500px;height:1px;background:rgba(255,255,255,.08)}
.copyright{left:0;width:684px;top:1172px;text-align:center;font-family:"Roboto",sans-serif;font-size:6.3px;letter-spacing:1.2px;color:var(--white)}
</style>
</head>
<body>

<header class="abs site-header">
  <div class="abs brand"><span class="brand-mark"></span>VARDELIX</div>
  <nav class="abs main-nav">
    <div class="nav-item is-active"><svg viewBox="0 0 10 10"><path d="M5 1 1 5h1.5v4h2V6.5h1V9h2V5H9z" fill="#fff"/></svg>Home</div>
    <div class="nav-item"><svg viewBox="0 0 10 10"><circle cx="5" cy="3" r="2.3" fill="#222"/><path d="M1 10c0-3 2-4.5 4-4.5s4 1.5 4 4.5z" fill="#222"/></svg>About us</div>
    <div class="nav-item"><svg viewBox="0 0 10 10"><circle cx="5" cy="5" r="5" fill="#222"/><text x="5" y="7.8" font-size="7" text-anchor="middle" fill="#fff" font-family="Arial">?</text></svg>FAQs</div>
    <div class="nav-item"><svg viewBox="0 0 10 10"><circle cx="5" cy="5" r="4" fill="none" stroke="#222" stroke-width="2"/><circle cx="5" cy="5" r="1.5" fill="#222"/></svg>Support</div>
  </nav>
</header>

<section class="abs hero" role="img" aria-label="Photo of a hand holding out a blue debit card"></section>
<h1 class="abs hero-title">FROM <strong>CREDIT CARD</strong> TO <strong>QUORBIT</strong><br>IN SECONDS</h1>
<p class="abs hero-sub">SIMPLE, TRUSTED, LOW FEE DIGITAL MONEY PLATFORM</p>
<a class="abs btn-learn">LEARN MORE <svg width="7" height="7" viewBox="0 0 10 10"><circle cx="5" cy="5" r="5" fill="#3277b5"/><path d="M4 3l2 2-2 2" stroke="#fff" stroke-width="1.5" fill="none"/></svg></a>
<div class="abs slider-arrow prev"><svg width="8" height="10" viewBox="0 0 8 10"><path d="M6 1 2 5l4 4" stroke="#3277b5" stroke-width="2.2" fill="none"/></svg></div>
<div class="abs slider-arrow next"><svg width="8" height="10" viewBox="0 0 8 10"><path d="M2 1l4 4-4 4" stroke="#3277b5" stroke-width="2.2" fill="none"/></svg></div>

<section class="abs features">
  <div class="feature">
    <svg viewBox="0 0 42 42" fill="none" stroke="#fff" stroke-width="2.5"><path d="M8 18a14 14 0 0 1 26-6"/><path d="M34 6v7h-7"/><path d="M34 24a14 14 0 0 1-26 6"/><path d="M8 36v-7h7"/><path d="M25 15c-1-2-7-2-7 1s7 2 7 6-6 3-7 1M21 12v18"/></svg>
    <p>Instantely exchange your dollars for Quorbit</p>
  </div>
  <div class="feature">
    <svg viewBox="0 0 42 42" fill="none" stroke="#fff" stroke-width="2.5"><rect x="5" y="10" width="30" height="26" rx="3"/><path d="M35 19h-7a4 4 0 0 0 0 8h7z"/><circle cx="22" cy="9" r="5" fill="#fff" stroke="none"/></svg>
    <p>Real time refunds receipt, you get your own digital wallet</p>
  </div>
  <div class="feature">
    <svg viewBox="0 0 42 42" fill="none" stroke="#fff" stroke-width="2.5"><circle cx="21" cy="22" r="16"/><ellipse cx="21" cy="22" rx="7" ry="16"/><path d="M5 22h32M8 14h26M8 30h26"/><circle cx="34" cy="9" r="4" fill="#fff"/></svg>
    <p>Global freedom to push quorb to whereever you want.</p>
  </div>
  <div class="feature">
    <svg viewBox="0 0 42 42" fill="none" stroke="#fff" stroke-width="2.5"><rect x="14" y="6" width="26" height="17" rx="2"/><path d="M14 12h26M30 18h6"/><path d="M2 30l8-8h10l-6 6h8l-6 8H2"/></svg>
    <p>Click here to purchase quorb</p>
  </div>
</section>

<h2 class="abs section-title why-title"><span class="lead">WHY</span> <span class="rest">QUORBIT?</span></h2>

<section class="abs benefits"></section>
<ul class="abs benefit-list">
  <li>Easily transactable</li>
  <li>Great upside value proposition</li>
  <li>Super low transaction speed</li>
  <li>Revolution tranaction payout system</li>
  <li>Master nodes</li>
</ul>
<a class="abs btn-primary">PUSH FOR SALMON <svg width="8" height="8" viewBox="0 0 10 10"><circle cx="5" cy="5" r="5" fill="#fff"/><path d="M4 3l2 2-2 2" stroke="#3277b5" stroke-width="1.5" fill="none"/></svg></a>
<div class="abs video-media" role="img" aria-label="Video still of hands typing on a laptop over coin stacks and a market chart"></div>

<section class="abs testimonials" role="img" aria-label="Faded background of customer portraits"></section>
<h2 class="abs section-title testi-title"><span class="lead">WHY</span> <span class="rest">QUORBIT?</span></h2>

<div class="abs testi-card" style="left:92px"><div class="quote">“</div><p>I was able to use my card to buy cash in minutes, so happy</p><cite>- Steve</cite></div>
<div class="abs testi-card" style="left:263px"><div class="quote">“</div><p>The site is so easy, free sign up, enter card with how much Quorb you want, open your new wallet and push to any other quorbit wallet</p><cite>- Laura</cite></div>
<div class="abs testi-card" style="left:434px"><div class="quote">“</div><p>As a newbie to crypto I was able to purchase my quorbit with my credicard,, so easy!</p><cite>- Matt</cite></div>
<div class="abs avatar" style="left:135px" role="img" aria-label="Portrait of Steve"></div>
<div class="abs avatar" style="left:306px" role="img" aria-label="Portrait of Laura"></div>
<div class="abs avatar" style="left:477px" role="img" aria-label="Portrait of Matt"></div>

<footer class="abs site-footer"></footer>
<nav class="abs footer-nav"><span>HOME</span><span>ABOUT US</span><span>FAQS</span><span>SUPPORT</span><span>PRIVACY POLICY</span></nav>
<div class="abs footer-rule"></div>
<p class="abs copyright">© 2018 VARDELIX SECURE. ALL RIGHTS RESERVED.</p>

</body>
</html>
```